A single page website & logo required for a Field Service Management Application

Name of the project - CrewTallo

We are software developers and we have a Field Service Management application ready. This software is all about optimizing the businesses that send their staff to various sites to provide service. Scheduling, creating jobs, quotes & invoices are a few salient features of it. It also has an accompanying Android & iPhone/iPad versions that will be used by the technicians.

More details can be provided, if needed.

After this web design project ends, the winning designer will be awarded the budget for the logo design through a 1on1 project.

Reason: I need to get the designs approved from my boss and he is currently overseas and is very busy. And hence I need the timeline to be extended.

Target Market(s)

All the Companies all over the world that send their staff to various sites to provide service.

Industry/Entity Type

Software

Logo Text

CrewTallo

Number of Pages Required

1 page

Font styles to use
Serif
Sans Serif

Requirements
Must have
• We would like to have the following components in the design:
• 1. Slider
• 2. Features of the software
• 3. Pricing Details
• 4. FAQs
• 5. Suitable for (Shows a list of all industries that our software is suitable for)
Nice to have
• A section with the background of a technician using our app on a mobile device (Screenshot can be provided)
Should not have
• Gaudy fonts and stereotypical designs

```html
<!DOCTYPE html>
<html lang="en">
<head>
<meta charset="utf-8">
<title>Field Service Management</title>
<link href="https://fonts.googleapis.com/css2?family=Ubuntu:wght@400;500;700&family=Source+Sans+3:wght@400;600&display=swap" rel="stylesheet">
<style>
:root{
  --navy:#1d3a66;
  --orange:#f26a22;
  --blue:#2f86d2;
  --hero:#4a95cc;
  --page:#e6e6e6;
  --tabbar:#b8b8b8;
  --text:#2b2b2b;
  --footer:#5b5b5b;
  --cyan:#35b8e8;
}
*{box-sizing:border-box;margin:0;padding:0}
html,body{width:953px;height:1200px;overflow:hidden}
body{position:relative;background:var(--page);font-family:"Source Sans 3",sans-serif;color:var(--text)}
.abs{position:absolute}
.header{left:0;top:0;width:953px;height:66px;background:linear-gradient(#fff,#f0f0f0)}
.brand{left:64px;top:2px;display:flex;align-items:center;gap:12px}
.brand-mark{width:60px;height:60px;border-radius:50%;background:#e3c068}
.brand-name{font-family:"Ubuntu",sans-serif;font-weight:500;font-size:24px;color:var(--navy)}
.contact-row{right:60px;top:14px;display:flex;gap:22px;font-size:12px;color:#333;align-items:center}
.contact-row span{display:flex;align-items:center;gap:6px}
.head-links{right:68px;top:40px;display:flex;align-items:center;font-family:"Ubuntu",sans-serif;font-weight:500;font-size:15px}
.head-links .link{color:var(--blue);margin-right:12px}
.head-links .order{background:var(--orange);color:#fff;padding:5px 6px}
.hero{left:0;top:66px;width:953px;height:332px;background:var(--hero)}
.hero h1{position:absolute;left:64px;top:64px;width:420px;font-family:"Ubuntu",sans-serif;font-weight:500;font-size:29px;line-height:35px;color:#fff}
.arrow{position:absolute;top:156px}
.devices{position:absolute;left:504px;top:54px;width:372px;height:232px;border-radius:10px;background:linear-gradient(135deg,#1f1f1f,#3c3c3c 55%,#e8c51f 56%,#d83a1f)}
.platforms{position:absolute;left:554px;top:258px;display:flex;gap:18px}
.platforms div{width:22px;height:22px;border-radius:3px}
.tabs{left:0;top:398px;width:953px;height:56px;background:var(--tabbar)}
.tab{position:absolute;top:0;height:56px;display:flex;align-items:center;justify-content:center;gap:8px;font-family:"Ubuntu",sans-serif;font-weight:500;font-size:20px;color:#fff;border-left:1px solid #d0d0d0}
.tab b{color:var(--orange);font-weight:500}
.tab.active{background:#fff;color:var(--blue);border:none}
.panel{left:64px;top:454px;width:825px;height:628px;background:#fff}
.panel h2{position:absolute;left:0;top:30px;width:825px;text-align:center;font-family:"Ubuntu",sans-serif;font-weight:500;font-size:20px;color:var(--blue)}
.panel h2 b{color:var(--orange);font-weight:500}
.rule{position:absolute;left:8px;top:58px;width:808px;height:1px;background:#aaa}
.lead{position:absolute;left:40px;top:72px;width:745px;text-align:center;font-family:"Ubuntu",sans-serif;font-size:16px;line-height:21px;color:var(--navy)}
.intro{position:absolute;left:10px;top:128px;width:805px;font-size:12.3px;line-height:18px}
.intro ol{margin-left:2px;list-style:none}
.intro .hl{color:var(--blue)}
.intro p.gap{margin-top:6px}
.col{position:absolute;font-size:11.4px;line-height:14px}
.col h3{font-weight:400;font-size:14px;color:var(--orange);margin-bottom:1px}
.col .desc{font-size:12.6px;line-height:14.2px;margin-bottom:6px}
.checks{list-style:none}
.checks li{position:relative;padding-left:12px}
.checks li::before{content:"✓";position:absolute;left:0;top:0;color:var(--blue);font-weight:600}
.subs{list-style:none;margin:3px 0 4px 22px}
.subs li{padding-left:10px;position:relative}
.subs li::before{content:"";position:absolute;left:0;top:4px;width:5px;height:5px;border:1px solid var(--blue);border-radius:50%}
.col.right .checks li{margin-bottom:7px}
.footer{left:0;top:1111px;width:953px;height:89px;background:var(--footer)}
.copy{position:absolute;left:64px;top:32px;font-family:"Ubuntu",sans-serif;font-weight:500;font-size:15px;color:#fff;display:flex;align-items:center;gap:6px}
.privacy{position:absolute;left:287px;top:33px;font-family:"Ubuntu",sans-serif;font-size:15px;color:var(--cyan)}
.foot-btn{position:absolute;top:24px;height:33px;width:124px;display:flex;align-items:center;justify-content:center;font-family:"Ubuntu",sans-serif;font-weight:500;font-size:16px;color:#fff}
</style>
</head>
<body>
<header class="abs header">
  <div class="abs brand"><div class="brand-mark"></div><div class="brand-name">Field Service Management</div></div>
  <div class="abs contact-row">
    <span><svg width="14" height="14" viewBox="0 0 14 14"><rect width="14" height="14" rx="2" fill="#5aa05a"/><path d="M4 3l2 2-1 1c.6 1.3 1.7 2.4 3 3l1-1 2 2-1.5 1.5C6 11 3 8 2.5 4.5z" fill="#fff"/></svg>+91 800 555 0192</span>
    <span><svg width="20" height="14" viewBox="0 0 20 14"><rect x=".5" y=".5" width="19" height="13" fill="none" stroke="#999"/><path d="M.5.5l9.5 8 9.5-8" fill="none" stroke="#999"/></svg>hello@rolvanesoft.com</span>
  </div>
  <div class="abs head-links"><span class="link">CONTACT US</span><span class="order">ORDER NOW</span></div>
</header>

<section class="abs hero">
  <svg class="arrow" style="left:14px" width="18" height="50" viewBox="0 0 18 50"><path d="M16 2L3 25l13 23" fill="none" stroke="#fff" stroke-width="2"/></svg>
  <h1>Field Service Management (FSM) allows you to schedule, optimize and service your customer in an organized and timely manner.</h1>
  <div class="devices" role="img" aria-label="Phones and tablet showing the job schedule app screens"></div>
  <div class="platforms"><div style="background:#8cc34a"></div><div style="background:#2aa3e0"></div><div style="background:#e4582a"></div></div>
  <svg class="arrow" style="left:922px" width="18" height="50" viewBox="0 0 18 50"><path d="M2 2l13 23L2 48" fill="none" stroke="#fff" stroke-width="2"/></svg>
</section>

<nav class="abs tabs">
  <div class="tab active" style="left:64px;width:211px">
    <svg width="30" height="30" viewBox="0 0 30 30"><circle cx="15" cy="15" r="15" fill="var(--navy)"/><path d="M8 21h14M9 19v-4M13 19v-6M17 19v-3M21 19v-8M9 14l4-4 4 3 5-5" stroke="#fff" stroke-width="2" fill="none"/></svg>
    <span><b>FSM</b> Features</span></div>
  <div class="tab" style="left:275px;width:218px">
    <svg width="30" height="30" viewBox="0 0 30 30"><rect width="30" height="30" rx="3" fill="#2a8fd6"/><text x="15" y="23" text-anchor="middle" font-size="22" font-weight="700" fill="#fff" font-family="Ubuntu,sans-serif">$</text></svg>
    <span><b>FSM</b> Price Plan</span></div>
  <div class="tab" style="left:493px;width:226px">
    <svg width="26" height="24" viewBox="0 0 26 24"><path d="M1 7L13 1l12 6z" fill="#2a6fb8"/><path d="M3 9h20M4 10v10M8 10v10M12 10v10M16 10v10M20 10v10M2 22h22" stroke="#2a6fb8" stroke-width="2.4"/></svg>
    <span><b>FSM</b> Suitable for</span></div>
  <div class="tab" style="left:719px;width:170px">
    <svg width="32" height="32" viewBox="0 0 32 32"><circle cx="16" cy="16" r="16" fill="#2ab3ec"/><text x="16" y="24" text-anchor="middle" font-size="22" font-weight="700" fill="#fff" font-family="Ubuntu,sans-serif">?</text></svg>
    <span><b>FSM</b> FAQ</span></div>
</nav>

<main class="abs panel">
  <h2>Features of <b>FSM</b></h2>
  <div class="rule"></div>
  <p class="lead">Rolvane's Field Service Management Solution is a complete end-to-end solution for companies having to send workforce for installation, doing on-site service/install and others</p>
  <div class="intro">
    <p>In order to help you in managing the mobile field service frenzy, we have come up with a solution that comes in two stages.</p>
    <ol>
      <li>1. <span class="hl">The Cloud Solution</span> – This part of the solution is for the admin.</li>
      <li>2. <span class="hl">The Mobile Application</span> – Each of your technicians will be able to manage the jobs assigned to him/her.</li>
    </ol>
    <p class="gap">The integration between these two segments of the solution is so seamless, that it creates an extremely profitable solution for you right away.</p>
  </div>

  <svg class="abs" style="left:30px;top:214px" width="118" height="70" viewBox="0 0 118 70"><path d="M22 66C8 66 3 56 5 48s10-13 18-11c0-12 10-20 20-17 4-12 18-18 30-13 9 4 13 12 12 21 10-3 22 4 24 15s-6 23-19 23z" fill="none" stroke="#1a5aa3" stroke-width="4"/></svg>
  <svg class="abs" style="left:700px;top:220px" width="78" height="78" viewBox="0 0 78 78"><circle cx="39" cy="39" r="37" fill="none" stroke="var(--cyan)" stroke-width="2"/><g fill="none" stroke="var(--cyan)" stroke-width="2"><rect x="13" y="28" width="13" height="22" rx="2"/><rect x="33" y="28" width="13" height="22" rx="2"/><rect x="53" y="28" width="13" height="22" rx="2"/></g><path d="M27 39h5M47 39h5" stroke="var(--cyan)" stroke-dasharray="1 2"/></svg>

  <div class="col" style="left:9px;top:289px;width:370px">
    <h3>Features of FSM Cloud Solution</h3>
    <p class="desc">Our Cloud solution has the best-in-breed features that empower you with the complete control of the whole process. Our Cloud Solution is leveraged to transform your Enterprise into a much, much better one. It allows you to:</p>
    <ul class="checks">
      <li>Advanced CRM – Manage all your leads and customer/contacts within the application</li>
      <li>Quote Management – Send quotes to the customer directly from the system in a clean PDF template with your own design, logo</li>
      <li>Job Management – Convert quotes to become a contract (job) and assign
        <ul class="subs">
          <li>Allows you to manage visits – Single or Recurring</li>
          <li>Inventory to be used during the visit with low level stock alerts</li>
          <li>Team who will do the Job</li>
          <li>Invoicing, Payment Receipts, Export to Accounting Packages</li>
        </ul></li>
      <li>Service your clients in the order of the nearby places –Address-based Scheduling lowers the travel time and also the fuel consumption. (Service more number of clients in that saved travel time.)</li>
      <li>Track the time duration taken by the technicians to complete each of their jobs</li>
      <li>Pay Technicians per visit – generate report per Technician</li>
      <li>Manage warehouse with stock alerts, purchase and stock history</li>
      <li>Generate 100s of reports with Customize Report options</li>
    </ul>
  </div>

  <div class="col right" style="left:447px;top:289px;width:370px">
    <h3>Features of FSM Mobile App</h3>
    <p class="desc" style="margin-top:6px;margin-bottom:12px">By integrating our Cloud solution with this App, you will be making your technicians proactively efficient. You will be cutting down on the temporal overheads by reducing the paperwork and unnecessary detours. Most importantly, you will be keeping them streamlined to the workflow. This Mobile solution will allow them to</p>
    <ul class="checks">
      <li>Login and see their schedules from anywhere</li>
      <li>See the start and end time of each job</li>
      <li>See the high priority tasks that they have to start with immediately</li>
      <li>Mark the job as “Completed” once they are done with it (Which you will be seeing on the Cloud Solution)</li>
      <li>Create new tasks on-the-go and charge the client appropriately – Helps when the technician has to work on any emergency tasks which were not scheduled by you. It also helps maintain transparency.</li>
      <li>View the changes that you make on the cloud solution in the form of notifications.</li>
    </ul>
  </div>
</main>

<footer class="abs footer">
  <div class="copy"><svg width="16" height="16" viewBox="0 0 16 16"><circle cx="8" cy="8" r="7" fill="none" stroke="#fff" stroke-width="1.2"/><path d="M10.5 6a3 3 0 1 0 0 4" fill="none" stroke="#fff" stroke-width="1.2"/></svg>All Rights Researved 2015</div>
  <div class="privacy">Privacy Policy</div>
  <div class="foot-btn" style="left:640px;background:var(--navy)">CONTACT US</div>
  <div class="foot-btn" style="left:764px;background:var(--orange)">ORDER NOW</div>
</footer>
</body>
</html>
```